BRWN Coaching Website

I would like someone to design my website. I have an existing site which is really basic and needs an overhaul. I have attached a powerpoint with all the information I require. I am flexible with the design and layout and am ok with graphics being added to enhance the attractiveness of the site.

```html
<!DOCTYPE html>
<html lang="en">
<head>
<meta charset="utf-8">
<title>BRWN Coaching</title>
<link rel="stylesheet" href="https://fonts.googleapis.com/css2?family=Abel&family=Questrial&display=swap">
<style>
:root{
  --navy:#0d3d6b;
  --orange:#f26a10;
  --grey-band:#b0b0b0;
  --light:#eeeeee;
  --border:#dedede;
  --text-soft:#a8a8a8;
  --footer:#2b2b2b;
  --footer-bottom:#3a3a3a;
  --footer-text:#9a9a9a;
}
*{margin:0;padding:0;box-sizing:border-box}
html,body{width:941px;height:1200px;overflow:hidden;background:#fff}
body{position:relative;font-family:Arial,Helvetica,sans-serif;color:#333}
.abs{position:absolute}
.brand{font-family:'Questrial',sans-serif;color:var(--navy);display:flex;align-items:center;gap:7px;white-space:nowrap}
.brand .dot{width:9px;height:9px;background:var(--orange)}
.header-brand{left:87px;top:30px;font-size:20px}
.contact-line{font-family:'Abel',sans-serif;color:var(--navy);font-size:15px;display:flex;align-items:center;gap:10px}
.contact-phone{left:643px;top:15px}
.contact-mail{left:643px;top:35px}
.social{display:flex;gap:7px}
.social span{width:15px;height:15px;display:block}
.social .s1{background:#2d6aa8}.social .s2{background:#2aa3dc}.social .s3{background:#d64a34}
.header-social{left:803px;top:62px}
.nav{left:0;top:93px;width:941px;height:36px;background:var(--navy);display:flex}
.nav a{font-family:'Abel',sans-serif;color:#fff;font-size:11.5px;text-decoration:none;text-transform:uppercase;line-height:36px;position:absolute;top:0}
.nav .active{background:var(--orange);width:80px;text-align:center}
.hero{left:88px;top:140px;width:767px;height:278px;border:1px solid var(--border);background:#fff;box-shadow:0 10px 10px -6px rgba(0,0,0,.18)}
.hero svg{position:absolute;left:0;top:0}
.hero-brand{left:510px;top:44px;font-size:30px}
.hero-services{font-family:'Questrial',sans-serif;color:var(--orange);font-size:16px}
.hero-services span::before{content:"› ";font-weight:bold}
.btn{background:var(--navy);color:#fff;font-family:'Questrial',sans-serif;text-align:center;text-transform:uppercase}
.btn-book{left:482px;top:213px;width:198px;height:37px;line-height:37px;font-size:13px}
.welcome{left:0;top:433px;width:941px;height:104px;background:var(--grey-band);color:#fff;font-family:'Abel',sans-serif;font-size:14.5px;text-align:center;line-height:18px;padding-top:25px}
.card{width:182px;height:190px;border:1px solid var(--border);top:554px;text-align:center}
.card h2{font-family:'Abel',sans-serif;font-weight:normal;color:var(--orange);font-size:17px;text-transform:uppercase;margin-top:9px}
.card .circle{width:142px;height:142px;border-radius:50%;margin:8px auto 0;border:3px solid #f0f0f0}
.cta{left:88px;top:755px;width:767px;height:85px;background:var(--light)}
.cta p{position:absolute;left:70px;top:30px;font-family:'Abel',sans-serif;color:var(--navy);font-size:20px}
.cta .cta-btn{position:absolute;left:585px;top:18px;width:140px;height:48px;background:#fff;border:1px solid var(--border);font-family:'Abel',sans-serif;color:var(--navy);font-size:17px;text-align:center;line-height:46px}
.panel{top:852px;height:225px;border:1px solid var(--border)}
.bio-photo{left:12px;top:12px;width:116px;height:163px;background:linear-gradient(160deg,#7d8a6a,#4a3a30 55%,#e47a6e)}
.bio-text{left:141px;top:13px;width:228px;font-family:'Abel',sans-serif;color:var(--text-soft);font-size:14px;line-height:18px}
.btn-small{width:90px;height:32px;line-height:32px;font-size:14px;font-family:'Abel',sans-serif;top:184px}
.form label{position:absolute;left:12px;font-size:11.5px;color:#444}
.form .field{position:absolute;left:12px;width:355px;height:20px;background:#eee;border:1px solid #ccc;font-size:11px;font-style:italic;color:#aaa;padding:3px 4px}
.footer{left:0;top:1090px;width:941px;height:85px;background:var(--footer);border-top:2px solid #d6d6d6}
.footer-links{font-size:9px;color:var(--footer-text);text-transform:uppercase;line-height:16px}
.divider{width:1px;height:56px;background:#555;top:15px}
.footer-brand{left:405px;top:30px;font-size:20px;color:#bbb}
.footer-brand .dot{background:#888}
.footer-contact{font-size:9px;color:var(--footer-text);display:flex;align-items:center;gap:8px}
.footer-bottom{left:0;top:1175px;width:941px;height:25px;background:var(--footer-bottom);color:#aaa;font-size:9px;text-align:center;line-height:26px}
</style>
</head>
<body>

<header>
  <div class="abs brand header-brand"><span class="dot"></span>BRWN Coaching</div>
  <div class="abs contact-line contact-phone">
    <svg width="16" height="14" viewBox="0 0 16 14"><path d="M2 4 Q8 0 14 4 L12 6 L10 5 L10 4 Q8 3 6 4 L6 5 L4 6 Z" fill="#0d3d6b"/><rect x="4" y="7" width="8" height="6" rx="1" fill="#0d3d6b"/></svg>
    <span>1300 555 019</span>
  </div>
  <div class="abs contact-line contact-mail" style="top:36px">
    <svg width="16" height="12" viewBox="0 0 16 12"><rect x="1" y="1" width="14" height="10" fill="#0d3d6b"/><path d="M1 1 L8 7 L15 1" stroke="#fff" fill="none" stroke-width="1.2"/></svg>
    <span>jane.marlow@brwncoaching.com</span>
  </div>
  <div class="abs social header-social"><span class="s1"></span><span class="s2"></span><span class="s3"></span></div>
</header>

<nav class="abs nav">
  <a class="active" style="left:87px">Home</a>
  <a style="left:200px">Individual Coaching</a>
  <a style="left:346px">Group Work</a>
  <a style="left:458px">Resources</a>
  <a style="left:567px">Inspiration Booth</a>
  <a style="left:704px">About</a>
  <a style="left:789px">Contact</a>
</nav>

<section class="abs hero">
  <svg width="767" height="278" viewBox="0 0 767 278">
    <defs>
      <linearGradient id="heroPhoto" x1="0" y1="0" x2="1" y2="1">
        <stop offset="0" stop-color="#f1f1f1"/><stop offset=".5" stop-color="#d9c2b0"/><stop offset="1" stop-color="#eeeeee"/>
      </linearGradient>
    </defs>
    <path role="img" aria-label="Photo of a smiling young girl lying on white bedding" d="M3 3 H478 Q372 80 344 275 H3 Z" fill="url(#heroPhoto)"/>
    <path d="M492 3 Q385 80 356 275" stroke="#f26a10" stroke-width="9" fill="none"/>
    <path d="M482 3 Q376 80 347 275" stroke="#0d3d6b" stroke-width="5" fill="none"/>
  </svg>
  <div class="abs brand hero-brand"><span class="dot"></span>BRWN Coaching</div>
  <div class="abs hero-services" style="left:421px;top:130px"><span>Life Coaching</span></div>
  <div class="abs hero-services" style="left:608px;top:130px"><span>Career Coaching</span></div>
  <div class="abs hero-services" style="left:421px;top:158px"><span>Leadership Coaching</span></div>
  <div class="abs hero-services" style="left:608px;top:159px"><span>Group Coaching</span></div>
  <div class="abs btn btn-book">Book Your Session</div>
</section>

<section class="abs welcome">
  Welcome to BRWN Coaching where we put a new perspective on the way you work, live and play.<br>
  Through our programs you will learn new skills &amp; techniques to enable you to break through the barriers that have kept you from<br>
  reaching your full potential up to now.
</section>

<section>
  <article class="abs card" style="left:88px">
    <h2>Individual Coaching</h2>
    <div class="circle" role="img" aria-label="Photo of a woman in a white blouse" style="background:linear-gradient(180deg,#e8e8e8,#d8c7b8 60%,#f4f4f4)"></div>
  </article>
  <article class="abs card" style="left:283px">
    <h2>Group Work</h2>
    <div class="circle" role="img" aria-label="Photo of colleagues working together at a table" style="background:linear-gradient(180deg,#7fb6d8,#c9a58c 55%,#5c9cc8)"></div>
  </article>
  <article class="abs card" style="left:478px">
    <h2>Resources</h2>
    <div class="circle" role="img" aria-label="Photo of a group of people in different work uniforms" style="background:linear-gradient(180deg,#f2f2f2,#b9a392 50%,#3a3a3a)"></div>
  </article>
  <article class="abs card" style="left:673px">
    <h2>Inspiration Booth</h2>
    <div class="circle" role="img" aria-label="Photo of a woman with raised arms in a golden field" style="background:linear-gradient(180deg,#f7f7f7,#e9dcc0 50%,#d9a24a)"></div>
  </article>
</section>

<section class="abs cta">
  <p>Get your free 30 minute introductory coaching session</p>
  <div class="cta-btn">CLICK HERE</div>
</section>

<section class="abs panel" style="left:88px;width:377px">
  <div class="abs bio-photo" role="img" aria-label="Portrait photo of Jane Marlow"></div>
  <p class="abs bio-text">Jane Marlow is a full time working Mum who believes that life is what you make it. She has experience in a variety of industries including Banking &amp; Finance, Telecommunications, Hospitality, Manufacturing and Farming. Jane spent three years working abroad in England, Scotland, Spain and Canada.</p>
  <div class="abs btn btn-small" style="left:275px">MORE</div>
</section>

<section class="abs panel form" style="left:478px;width:377px">
  <label style="top:14px">Name:</label>
  <div class="field" style="top:28px">Enter Name</div>
  <label style="top:56px">Email:</label>
  <div class="field" style="top:70px">Enter Email</div>
  <label style="top:98px">Message:</label>
  <div class="field" style="top:112px;height:57px">Enter Your Message</div>
  <div class="abs btn btn-small" style="left:276px">SEND</div>
</section>

<footer>
  <div class="abs footer">
    <div class="abs footer-links" style="left:87px;top:12px">Home<br>Individual Coaching<br>Group Work<br>Resources</div>
    <div class="abs footer-links" style="left:199px;top:12px">Inspiration Booth<br>About<br>Contact</div>
    <div class="abs divider" style="left:339px"></div>
    <div class="abs brand footer-brand"><span class="dot"></span>BRWN Coaching</div>
    <div class="abs divider" style="left:602px"></div>
    <div class="abs footer-contact" style="left:609px;top:14px">
      <svg width="12" height="10" viewBox="0 0 16 14"><path d="M2 4 Q8 0 14 4 L12 6 L10 5 L10 4 Q8 3 6 4 L6 5 L4 6 Z" fill="#999"/><rect x="4" y="7" width="8" height="6" rx="1" fill="#999"/></svg>1300 555 019</div>
    <div class="abs footer-contact" style="left:609px;top:30px">
      <svg width="12" height="9" viewBox="0 0 16 12"><rect x="1" y="1" width="14" height="10" fill="#999"/><path d="M1 1 L8 7 L15 1" stroke="#2b2b2b" fill="none" stroke-width="1.2"/></svg>jane.marlow@brwncoaching.com</div>
    <div class="abs social" style="left:610px;top:47px;gap:4px"><span class="s1" style="width:17px;height:17px"></span><span class="s2" style="width:17px;height:17px"></span><span class="s3" style="width:17px;height:17px"></span></div>
  </div>
  <div class="abs footer-bottom">© 2014 Bright Rowan Coaching. All Rights Reserved.</div>
</footer>

</body>
</html>
```